Casa Vero Inspections Business Card

I need a business card for my new company. The company is going to provide home inspections. The name of the company is Casa Vero Inspections. I am not sure if I want a single sided card or a double. I have a logo already that I want to incorporate into the card design. I was wondering if I should incorporate a catch phrase on my card or not. If I did the phrase would be "Clear Answers for Every Home You Buy" but i am unsure how or if to use it on a card. The following information needs to be on the card.
Home Inspection
My Name: Marcus T. Wolford Phone Number: 555-301-7762 Email: mwolford@casaveroinspections.com Website: www.casaveroinspections.com NY HI License # 27300519462

```html
<!DOCTYPE html>
<html lang="en">
<head>
<meta charset="utf-8">
<title>Casa Vero Inspections – Business Card</title>
<link href="https://fonts.googleapis.com/css2?family=Open+Sans:wght@400;600;800&display=swap" rel="stylesheet">
<style>
  :root {
    --stage: #3a3a3a;
    --card: #141414;
    --white: #ffffff;
    --soft-white: #e6e6e6;
    --sky: #6ec1ec;
  }
  * { margin: 0; padding: 0; box-sizing: border-box; }
  html, body { width: 1200px; height: 780px; overflow: hidden; }
  body {
    background: var(--stage);
    font-family: "Open Sans", Arial, sans-serif;
    display: flex;
    align-items: center;
    justify-content: center;
    gap: 40px;
  }
  .card {
    width: 540px;
    height: 308px;
    background: var(--card);
    border-radius: 18px;
    position: relative;
    overflow: hidden;
  }

  /* Brand name set as plain text */
  .brand {
    color: var(--white);
    font-weight: 800;
    text-transform: uppercase;
    line-height: 1.05;
    display: flex;
    align-items: center;
  }
  .brand-dot {
    width: 12px; height: 12px;
    background: var(--sky);
    margin-right: 12px;
    flex: none;
  }

  /* Front side */
  .card-front { display: flex; align-items: center; justify-content: center; }
  .card-front .brand { font-size: 40px; letter-spacing: 1px; }
  .card-front .brand-dot { width: 18px; height: 18px; margin-right: 18px; }

  /* Back side */
  .card-back .identity {
    position: absolute;
    left: 34px; top: 52px;
    width: 210px;
  }
  .card-back .brand { font-size: 24px; }
  .tagline {
    position: absolute;
    left: 34px; bottom: 40px;
    color: var(--soft-white);
    font-size: 12px;
    line-height: 1.5;
    white-space: nowrap;
  }
  .divider {
    position: absolute;
    left: 272px; top: 40px;
    width: 1px; height: 150px;
    background: var(--sky);
  }
  .contact {
    position: absolute;
    left: 296px; top: 48px;
  }
  .person-name {
    color: var(--sky);
    font-weight: 600;
    font-size: 21px;
    margin-bottom: 14px;
  }
  .contact-list { list-style: none; }
  .contact-list li {
    display: flex;
    align-items: center;
    gap: 8px;
    color: var(--soft-white);
    font-size: 12px;
    line-height: 1.9;
  }
  .contact-list svg { width: 12px; height: 12px; flex: none; }
  .license {
    position: absolute;
    left: 296px; bottom: 40px;
    color: var(--soft-white);
    font-size: 12px;
    line-height: 1.5;
    white-space: nowrap;
  }
</style>
</head>
<body>

  <section class="card card-back">
    <div class="identity">
      <div class="brand"><span class="brand-dot"></span><span>Casa Vero<br>Inspections</span></div>
    </div>
    <p class="tagline">Clear Answers for Every Home You Buy</p>
    <div class="divider"></div>
    <div class="contact">
      <h1 class="person-name">Marcus T. Wolford</h1>
      <ul class="contact-list">
        <li>
          <svg viewBox="0 0 24 24" fill="var(--sky)" aria-hidden="true"><path d="M6.6 10.8a15.1 15.1 0 0 0 6.6 6.6l2.2-2.2c.3-.3.7-.4 1-.2 1.1.4 2.3.6 3.6.6.6 0 1 .4 1 1V20c0 .6-.4 1-1 1A17 17 0 0 1 3 4c0-.6.4-1 1-1h3.5c.6 0 1 .4 1 1 0 1.3.2 2.5.6 3.6.1.3 0 .7-.2 1z"/></svg>
          555-301-7762
        </li>
        <li>
          <svg viewBox="0 0 24 24" fill="var(--sky)" aria-hidden="true"><path d="M2 5h20v14H2zm2 2v.5l8 5 8-5V7l-8 5z"/></svg>
          mwolford@casaveroinspections.com
        </li>
        <li>
          <svg viewBox="0 0 24 24" fill="none" stroke="var(--sky)" stroke-width="2" aria-hidden="true"><circle cx="12" cy="12" r="9"/><path d="M3 12h18M12 3c3 3 3 15 0 18M12 3c-3 3-3 15 0 18"/></svg>
          www.casaveroinspections.com
        </li>
      </ul>
    </div>
    <p class="license">NY HI License # 27300519462</p>
  </section>

  <section class="card card-front">
    <div class="brand"><span class="brand-dot"></span><span>Casa Vero<br>Inspections</span></div>
  </section>

</body>
</html>
```